Premium CBD/Hemp company needs packaging and label design

Verdant Oakfield, a premium CBD/Hemp company based in Scottsdale, Arizona is in need of a packaging and label design. We are launching with our flagship product which will be a 30 count capsule and will come in three functions: Pain Relief, Anxiety Support, and Sleep Support. For the purpose of this contest, please design packaging and label for our Anxiety Support product. Our products are physician formulated and all natural. Our main ingredient is CBD/Hemp and is complemented by specific herbs that synergistically work together to give the customer the most effective and desired result. We would like our branding to have a pharmaceutical look and feel with a focus on trust and transparency. We have uploaded our company logo that is to be used on both the packaging and label. We have also uploaded an executed branding questionnaire that will guide you to exactly what we are seeking to achieve as to the look and feel of our brand. Please feel free to contact us with any questions that you may have. The winner of this contest will have the opportunity to work with us on future projects as we will need packaging and label design for our entire Verdant Oakfield product line.

Target Market(s)

See attached branding questionnaire

Industry/Entity Type

Health And Wellness

Font styles to use
Sans Serif

Colors

Designer to choose colors to be used in the design.

Requirements
Must have
• See attached branding questionnaire; Please superimpose labels onto a cobalt blue capsule bottle (see attached)
• >>UPON REVIEW of the FIRST 8 designs, we really like the silver, mildly metallic label background in DESIGN # 21300528, we do not want metalic lettering as that would not look very "Pharmaceutical"
• >>We are in search of a look that is a bit more "Pharmaceutical" than a look that would be more commonly found in a Supplement Store
Nice to have
• "See attached branding questionnaire
Should not have
• See attached branding questionnaire; NO marijuana or cannabis plant on the packaging or label

```html
<!DOCTYPE html>
<html lang="en">
<head>
<meta charset="utf-8">
<title>Verdant Oakfield CBD Capsules – Label and Carton</title>
<link rel="stylesheet" href="https://fonts.googleapis.com/css2?family=Montserrat:wght@500;700;800&family=Arimo:wght@400;700&display=swap">
<style>
  :root {
    --brand-blue: #2b3e92;
    --brand-green: #23a04a;
    --band-green: #1e9c3f;
    --teal: #4fa7ac;
    --ink: #1c1c1c;
    --silver-light: #f4f4f7;
    --silver-mid: #e2e3ea;
    --silver-dark: #cfd1db;
    --page: #ffffff;
  }
  * { box-sizing: border-box; margin: 0; padding: 0; }
  html, body { width: 1200px; height: 1200px; overflow: hidden; background: var(--page); }
  .canvas { position: relative; width: 1200px; height: 1200px; }

  .brand { display: flex; align-items: center; gap: 12px; }
  .brand-dot { border-radius: 50%; border: 3px solid var(--brand-blue); flex: none; }
  .brand-name {
    font-family: "Montserrat", sans-serif; font-weight: 500;
    color: var(--brand-blue); white-space: nowrap; letter-spacing: 0.5px;
  }

  .product { font-family: "Montserrat", sans-serif; font-weight: 800; color: var(--brand-blue); line-height: 0.95; }
  .variant {
    display: inline-block; font-family: "Arimo", sans-serif; color: var(--brand-green);
    border: 2px solid var(--brand-green); white-space: nowrap;
  }
  .strength { font-family: "Arimo", sans-serif; font-weight: 700; color: var(--ink); }
  .supplement { font-family: "Arimo", sans-serif; color: var(--brand-green); }

  /* Bottle label, flat */
  .label {
    position: absolute; left: 150px; top: 390px; width: 440px; height: 400px;
    background: linear-gradient(100deg, var(--silver-mid) 0%, var(--silver-light) 40%, var(--silver-dark) 100%);
    padding: 40px 0 0 52px;
  }
  .label .brand-dot { width: 40px; height: 40px; }
  .label .brand-name { font-size: 26px; }
  .label .product-main { font-size: 62px; margin-top: 34px; }
  .label .product-sub { font-size: 27px; margin-top: 6px; }
  .label .variant { font-size: 17px; padding: 4px 8px; margin-top: 14px; }
  .label .meta { display: flex; align-items: baseline; gap: 10px; margin-top: 14px; }
  .label .strength { font-size: 17px; }
  .label .supplement { font-size: 12px; }
  .label .count { font-family: "Arimo", sans-serif; font-size: 13px; color: var(--ink); margin-top: 20px; }
  .label-band { position: absolute; left: 0; right: 0; bottom: 26px; height: 16px; background: var(--teal); }

  /* Carton front, flat */
  .carton {
    position: absolute; left: 650px; top: 250px; width: 400px; height: 700px;
    background: linear-gradient(95deg, var(--silver-light) 0%, var(--silver-mid) 60%, var(--silver-dark) 100%);
  }
  .carton .brand { position: absolute; left: 44px; top: 88px; }
  .carton .brand-dot { width: 54px; height: 54px; }
  .carton .brand-name { font-size: 32px; }
  .carton .product-main { position: absolute; left: 54px; top: 228px; font-size: 100px; }
  .carton .product-sub { position: absolute; left: 62px; top: 318px; font-size: 38px; }
  .carton .variant { position: absolute; left: 48px; top: 425px; font-size: 25px; padding: 10px 12px; }
  .carton .strength { position: absolute; left: 0; right: 0; top: 502px; text-align: center; font-size: 26px; }
  .carton .supplement { position: absolute; left: 0; right: 0; top: 556px; text-align: center; font-size: 24px; }
  .carton-band {
    position: absolute; left: 0; right: 0; bottom: 0; height: 86px; background: var(--band-green);
    display: flex; align-items: center; justify-content: center;
    font-family: "Arimo", sans-serif; font-size: 21px; color: #ffffff; letter-spacing: 0.5px;
  }
</style>
</head>
<body>
<main class="canvas">
  <section class="label" aria-label="Bottle label">
    <div class="brand"><span class="brand-dot"></span><span class="brand-name">Verdant Oakfield</span></div>
    <div class="product product-main">CBD</div>
    <div class="product product-sub">CAPSULES</div>
    <div class="variant">Anxiety &amp; Depression</div>
    <div class="meta"><span class="strength">750MG</span><span class="supplement">Dietary Supplement</span></div>
    <div class="count">30 CAPSULES PER BOTTLE</div>
    <div class="label-band"></div>
  </section>

  <section class="carton" aria-label="Carton front">
    <div class="brand"><span class="brand-dot"></span><span class="brand-name">Verdant Oakfield</span></div>
    <div class="product product-main">CBD</div>
    <div class="product product-sub">CAPSULES</div>
    <div class="variant">Anxiety &amp; Depression</div>
    <div class="strength">750MG</div>
    <div class="supplement">Dietary Supplement</div>
    <div class="carton-band">30 CAPSULES PER BOTTLE</div>
  </section>
</main>
</body>
</html>
```